Stationary and design update for my brand

I need new letterhead, a new business card, business envelope design, new keynote and powerpoint branded slides (16x9). I have logo samples in various styles and brand standards for fonts and colors.

Font styles to use
Sans Serif

```html
<!DOCTYPE html>
<html lang="en">
<head>
<meta charset="utf-8">
<title>Ridgeway Coaching – Business Cards</title>
<link rel="stylesheet" href="https://fonts.googleapis.com/css2?family=Jost:wght@400;500&family=Libre+Baskerville:wght@700&display=swap">
<style>
  :root {
    --backdrop: #3a322d;
    --orange: #ee8f1f;
    --paper: #f6f6f6;
    --ink: #3b3b3b;
    --white: #ffffff;
  }
  * { box-sizing: border-box; margin: 0; padding: 0; }
  html, body { width: 1200px; height: 716px; overflow: hidden; }
  body {
    background: var(--backdrop);
    font-family: "Jost", sans-serif;
    position: relative;
  }
  .card {
    position: absolute;
    top: 208px;
    width: 520px;
    height: 300px;
    overflow: hidden;
    box-shadow: 0 6px 16px rgba(0,0,0,0.45);
  }
  .card--front { left: 50px; background: var(--paper); color: var(--ink); }
  .card--back { left: 630px; background: var(--orange); color: var(--white); }

  .wordmark {
    font-family: "Jost", sans-serif;
    font-weight: 500;
    text-transform: uppercase;
    line-height: 1;
  }
  .wordmark__name { display: block; letter-spacing: 0.04em; }
  .wordmark__tag { display: block; letter-spacing: 0.06em; }

  .card--front .wordmark { position: absolute; left: 34px; top: 30px; color: var(--orange); }
  .card--front .wordmark__name { font-size: 34px; }
  .card--front .wordmark__tag { font-size: 7.5px; margin-top: 4px; }

  .holder { position: absolute; left: 34px; top: 104px; }
  .holder__name {
    font-family: "Libre Baskerville", serif;
    font-weight: 700;
    font-size: 15px;
    color: var(--orange);
  }
  .holder__creds { font-size: 10px; letter-spacing: 0.04em; }
  .holder__role, .holder__company, .holder__address { font-size: 11px; line-height: 1.45; }
  .holder__role { margin-top: 2px; }
  .holder__company { margin-top: 6px; }

  .contacts { position: absolute; left: 34px; top: 196px; list-style: none; font-size: 11px; line-height: 1.5; }
  .contacts li { display: flex; align-items: center; gap: 7px; }
  .contacts svg { width: 10px; height: 10px; fill: var(--orange); flex: none; }

  .band { position: absolute; left: 0; bottom: 0; width: 520px; height: 300px; }

  .card--back .wordmark { position: absolute; right: 40px; top: 118px; text-align: left; }
  .card--back .wordmark__name { font-size: 44px; }
  .card--back .wordmark__tag { font-size: 9.5px; margin-top: 6px; }
</style>
</head>
<body>

<section class="card card--front" aria-label="Business card front">
  <div class="wordmark">
    <span class="wordmark__name">Ridgeway</span>
    <span class="wordmark__tag">Coaching and Behavioral Consulting</span>
  </div>

  <div class="holder">
    <p class="holder__name">Daniel Hartwell-Moore, <span class="holder__creds">DMIN, PCC</span></p>
    <p class="holder__role">Owner | Trainer | Coach | Consultant</p>
    <p class="holder__company">Ridgeway Coaching &amp; Behavioral Consulting LLC</p>
    <p class="holder__address">4810 Alder Crest Dr. Millbrook, TX 75000</p>
  </div>

  <ul class="contacts">
    <li><svg viewBox="0 0 10 10"><path d="M2.5 0h5a1 1 0 0 1 1 1v8a1 1 0 0 1-1 1h-5a1 1 0 0 1-1-1V1a1 1 0 0 1 1-1zm0 1.5v6h5v-6z"/></svg>(555) 014-2290</li>
    <li><svg viewBox="0 0 10 10"><path d="M0 2h10v6H0zm1 .8v.4l4 2.6 4-2.6v-.4z"/></svg>daniel@ridgewaycbc.com</li>
    <li><svg viewBox="0 0 10 10"><circle cx="5" cy="5" r="5"/></svg>www.ridgewaycbc.com</li>
  </ul>

  <svg class="band" viewBox="0 0 520 300" aria-hidden="true">
    <path d="M250 300 C 330 262, 420 250, 520 228 L520 246 C 430 266, 350 282, 290 300 Z" fill="var(--orange)"/>
  </svg>
</section>

<section class="card card--back" aria-label="Business card back">
  <svg class="band" viewBox="0 0 520 300" aria-hidden="true">
    <path d="M70 0 L92 0 C 110 90, 170 180, 240 300 L210 300 C 150 200, 80 110, 70 0 Z" fill="var(--paper)"/>
  </svg>
  <div class="wordmark">
    <span class="wordmark__name">Ridgeway</span>
    <span class="wordmark__tag">Coaching and Behavioral Consulting</span>
  </div>
</section>

</body>
</html>
```